Events By Quellon

Weddings, Corporate, Special Events
Memorable Catering, Personalized Menus, Custom Layout & Designs
Professional Staff, Excellent Service
Our Mission is Turning YOUR Vision into a Reality

Dorrie Quellon, Principal Planner
ph. 202 555-0187 - fax 301-555-0142
Email - eventsbyquellon@mailhaven.net
Web - www.cateringbyquellon.net
cateringbyquellon@Instagram

Target Market(s)

All Brides, Corprate Business, Special Events

Industry/Entity Type

Hospitality

Contact Information for Business Card

clean but affective

Font styles to use
Serif
Sans Serif
Script

Colors

Designer to choose colors to be used in the design.

Requirements
Must have
• logo with tagline using colors that will enhance what
• some pictures of nice table scape, hors d'oevures, upscale foods......
Nice to have
• Event: Something that happens or is regarded as happening, an occurrence especially one of some importance.
Should not have
• Use Logo on both sides

```html
<!DOCTYPE html>
<html lang="en">
<head>
<meta charset="utf-8">
<title>Events By Quellon – Business Card</title>
<link rel="stylesheet" href="https://fonts.googleapis.com/css2?family=Cinzel:wght@400;600&family=Source+Sans+3:wght@400&display=swap">
<style>
  :root {
    --page: #e4e4e4;
    --teal: #1aa3b0;
    --grey: #808184;
    --ink: #2b2b2b;
    --card-white: #ffffff;
    --card-dark: #242122;
    --muted-light: #cfcfcf;
    --rule: #d9d9d9;
  }
  * { margin: 0; padding: 0; box-sizing: border-box; }
  html, body { width: 1200px; height: 802px; overflow: hidden; background: var(--page); }
  .stage { position: relative; width: 1200px; height: 802px; }
  .card {
    position: absolute; top: 274px; width: 442px; height: 265px; overflow: hidden;
    box-shadow: 0 3px 8px rgba(0,0,0,0.25);
  }
  .card--front { left: 136px; background: var(--card-white); }
  .card--back { left: 624px; background: var(--card-dark); }

  /* front */
  .front-mark { position: absolute; left: 0; top: 0; width: 200px; height: 265px; }
  .front-mark__ring { position: absolute; left: -55px; top: 6px; width: 160px; height: 160px;
    border: 6px solid var(--grey); border-radius: 50%; }
  .front-mark__name { position: absolute; left: 16px; top: 192px; width: 180px;
    font-family: "Cinzel", serif; font-weight: 600; font-size: 21px; line-height: 1.15; color: var(--teal); }

  .details { position: absolute; right: 23px; top: 30px; text-align: right;
    font-family: "Source Sans 3", sans-serif; color: var(--ink); }
  .details__name { font-family: "Cinzel", serif; font-weight: 400; font-size: 18px; line-height: 1; color: var(--teal); }
  .details__title { font-size: 13.5px; color: #555; line-height: 1.2; margin-top: 2px; }
  .contact { list-style: none; margin-top: 10px; font-size: 12.5px; line-height: 15.6px; }
  .contact li { display: flex; justify-content: flex-end; align-items: center; gap: 3px; }
  .contact svg { width: 10px; height: 10px; fill: var(--teal); }
  .details__rule { width: 176px; height: 1px; background: var(--rule); margin: 13px 0 0 auto; }
  .services { list-style: none; margin-top: 14px; font-size: 12.5px; line-height: 15.8px; }

  /* back */
  .back-mark { position: absolute; left: 50%; top: 40px; width: 46px; height: 46px; margin-left: -23px;
    border: 3px solid var(--grey); border-radius: 50%; }
  .back-name { position: absolute; left: 0; right: 0; top: 138px; text-align: center;
    font-family: "Cinzel", serif; font-weight: 600; font-size: 20px; color: var(--teal); line-height: 1; }
  .back-tagline { position: absolute; left: 0; right: 0; top: 163px; text-align: center;
    font-family: "Cinzel", serif; font-size: 7.5px; letter-spacing: 0.3px; color: var(--muted-light); }
  .mission { position: absolute; left: 0; right: 0; top: 182px; text-align: center;
    font-family: "Source Sans 3", sans-serif; font-size: 11.5px; letter-spacing: 0.2px; color: var(--muted-light); }
  .social { position: absolute; left: 60px; right: 60px; top: 217px; display: flex; align-items: center; gap: 6px;
    font-family: "Source Sans 3", sans-serif; font-size: 13px; color: var(--teal); }
  .social__line { flex: 1; height: 1px; background: #4a4748; }
  .social__dot { width: 13px; height: 13px; border-radius: 50%; background: #2b88b8; }
</style>
</head>
<body>
<main class="stage">
  <section class="card card--front" aria-label="Business card front">
    <div class="front-mark">
      <div class="front-mark__ring"></div>
      <div class="front-mark__name">Events By<br>Quellon</div>
    </div>
    <div class="details">
      <h1 class="details__name">Dorrie Quellon</h1>
      <p class="details__title">Principal Planner</p>
      <ul class="contact">
        <li>202 555-0187 <svg viewBox="0 0 10 10"><path d="M1 3 Q5 0 9 3 L8 4.5 L6.5 4 L6.5 3 Q5 2.5 3.5 3 L3.5 4 L2 4.5Z M2 5 H8 V9 H2Z"/></svg></li>
        <li>301-555-0142 <svg viewBox="0 0 10 10"><path d="M3 1 H7 V3 H3Z M1 4 H9 V7.5 H7.5 V9 H2.5 V7.5 H1Z"/></svg></li>
        <li>eventsbyquellon@mailhaven.net <svg viewBox="0 0 10 10"><path d="M1 2 H9 V8 H1Z M1.5 2.5 L5 5.5 L8.5 2.5" stroke="#fff" stroke-width="0.8"/></svg></li>
        <li>www.cateringbyquellon.net <svg viewBox="0 0 10 10"><circle cx="5" cy="5" r="4.5"/></svg></li>
      </ul>
      <div class="details__rule"></div>
      <ul class="services">
        <li>Weddings &nbsp;|&nbsp; Professional Staff</li>
        <li>Special Events &nbsp;|&nbsp; Corporate</li>
        <li>Memorable Catering</li>
        <li>Personalized Menus and Designs</li>
      </ul>
    </div>
  </section>

  <section class="card card--back" aria-label="Business card back">
    <div class="back-mark"></div>
    <h2 class="back-name">Events By Quellon</h2>
    <p class="back-tagline">Events Designed with You in Mind</p>
    <p class="mission">OUR MISSION IS TURNING YOUR VISION INTO A REALITY</p>
    <div class="social">
      <span class="social__line"></span>
      <span class="social__dot"></span>
      <span>cateringbyquellon@Instagram</span>
      <span class="social__line"></span>
    </div>
  </section>
</main>
</body>
</html>
```